Design eines Hausetiketts für traditionelles Weingut
Zielgruppe
Wir das Familienweingut Brosowski in Gimbsheim/Rheinhessen sind ein traditionelles Weingut das seine Reben selbst kultiviert und die Weine auch selbst ausbaut. Wir haben jeden Schritt in der Weinherstellung selbst in der Hand und vermarkten den Wein dann an unsere Privatkunden. Unsere Kundenstruktur sieht folgendermaßen aus: Wir haben 100% Privatkunden die unseren Wein konsumieren. Da jetzt die nächste Generation in den Weinbaubetrieb einsteigt und auch Ideen hat möchten wir ein Hausetikett einführen. Im Moment haben wir noch sehr viele unterschiedliche Etiketten und kein Hausetikett. Da die Verlagsetiketten immer seltener zu unseren Vorstellungen passen, möchten wir hier auf diesem Wege ein Hausetikett anfertigen lassen. Generell möchten wir unseren Außenauftritt komplett modernisieren. Sie können sich über die Vielfalt in unserem Betrieb unter www.weingut-brosowski-beispiel.de einen Überblick verschaffen. Langfristig gesehen wollen wir aber unsere Weinkarte verkleinern.
Aufgabenstellung
Wir haben uns vor ca. 1,5 Jahren hier auf dieser Website bereits ein Logo designen lassen. Es wäre schön wenn man das Logo bei den Entwürfen für die Etiketten berücksichtigen würde. Das wäre aber KEIN MUSS. Auch wäre es gut wenn man das ,,Wein' bei unserem Namen weglassen könnte.
Das Etikett sollte aus Vorder-und Rückenetikett bestehen und edel wirken. Vorne sollte die Rebsorte und die Geschmacksangabe stehen. Der Rest sollte auf das Rückenetikett.
Das Vorderetikett sollte ein richtiger Eyecatcher sein und im Supermarkt z.B. aus vielen anderen herausstechen. Das wäre ganz wichtig.
Man kann bei den Farben unterscheiden in 3 Konzepte.
Literwein als einsteiger Wein
Dann die Gutsweine und zum Schluss die Lagenweine. Alles Farblich oder im design etwas abgesetzt.

```html
<!DOCTYPE html>
<html lang="de">
<head>
<meta charset="utf-8">
<title>Brosowski Weißburgunder – Vorderetikett</title>
<link rel="stylesheet" href="https://fonts.googleapis.com/css2?family=Cinzel:wght@400&family=Courgette&display=swap">
<style>
  :root {
    --page-bg: #ffffff;
    --label-teal-dark: #1d6556;
    --label-teal: #23705f;
    --label-teal-light: #2f7f6d;
    --pattern-tone: #4e9584;
    --gold: #c9a24a;
    --gold-light: #e3c77a;
    --script-cream: #e9efe6;
  }
  html, body {
    margin: 0;
    padding: 0;
    width: 1200px;
    height: 1200px;
    overflow: hidden;
    background: var(--page-bg);
  }
  .canvas {
    position: relative;
    width: 1200px;
    height: 1200px;
  }
  .front-label {
    position: absolute;
    left: 126px;
    top: 50px;
    width: 948px;
    height: 1100px;
    background: linear-gradient(180deg, var(--label-teal-dark) 0%, var(--label-teal) 45%, var(--label-teal-light) 100%);
    overflow: hidden;
  }
  .clover-pattern {
    position: absolute;
    left: 0;
    right: 0;
    top: 420px;
    bottom: 0;
    background: linear-gradient(180deg, rgba(78,149,132,0) 0%, rgba(78,149,132,0.35) 40%, rgba(78,149,132,0.55) 100%);
  }
  .winery-name {
    position: absolute;
    top: 186px;
    left: 0;
    right: 0;
    margin: 0;
    text-align: center;
    font-family: "Cinzel", serif;
    font-weight: 400;
    font-size: 46px;
    letter-spacing: 1px;
    color: var(--gold);
  }
  .grape-variety {
    position: absolute;
    top: 318px;
    left: 0;
    right: 0;
    margin: 0;
    text-align: center;
    font-family: "Courgette", cursive;
    font-weight: 400;
    font-size: 84px;
    color: var(--script-cream);
  }
  .clover-emblem {
    position: absolute;
    left: 291px;
    top: 478px;
    width: 366px;
    height: 376px;
  }
  .taste {
    position: absolute;
    top: 930px;
    left: 0;
    right: 0;
    margin: 0;
    text-align: center;
    font-family: "Courgette", cursive;
    font-size: 52px;
    color: var(--script-cream);
  }
</style>
</head>
<body>
  <main class="canvas">
    <section class="front-label">
      <div class="clover-pattern" role="img" aria-label="Dezentes Muster aus kleinen Kleeblatt-Umrissen"></div>
      <h1 class="winery-name">BROSOWSKI</h1>
      <h2 class="grape-variety">Weißburgunder</h2>
      <svg class="clover-emblem" viewBox="0 0 366 376" role="img" aria-label="Goldenes vierblättriges Kleeblatt als zentrales Ornament">
        <defs>
          <radialGradient id="emblem-glow" cx="50%" cy="50%" r="50%">
            <stop offset="0%" stop-color="#1d6556"/>
            <stop offset="100%" stop-color="#236e5e"/>
          </radialGradient>
        </defs>
        <rect x="0" y="0" width="366" height="376" rx="40" fill="url(#emblem-glow)" opacity="0.6"/>
      </svg>
      <p class="taste">trocken</p>
    </section>
  </main>
</body>
</html>
```